Need Banners ....We make it Swift and Easy

We are a commercial printing shop and we do banners and posters. Want to place ads on Trellisgram and get people to hit a button to get a quote.You can use our logo or not. We want to attract new customers for our various services one service at a time. Need Banners needs to be big with "We make it Swift and Easy" as a tag line.

Target Market(s)

businesses

Font styles to use
Sans Serif

Colors

Designer to choose colors to be used in the design.

Requirements
Must have
• EYE CATCHING
Nice to have
• Very simple and eye catching. If this works I have 7 more to do with different works such as BROCHURES, MAILING SERVICES......

```html
<!DOCTYPE html>
<html lang="en">
<head>
<meta charset="utf-8">
<title>Need a Banner – SwiftPress</title>
<link href="https://fonts.googleapis.com/css2?family=Source+Sans+3:wght@400;700&display=swap" rel="stylesheet">
<style>
  :root {
    --bg: #000000;
    --headline: #3cee1e;
    --tagline: #ffffff;
    --brand: #e0403a;
    --plate: #ffffff;
    --glow-red: #8a1c2a;
    --glow-violet: #5a2a6e;
    --glow-blue: #2a3f8f;
  }
  * { margin: 0; padding: 0; box-sizing: border-box; }
  html, body {
    width: 1200px;
    height: 628px;
    overflow: hidden;
    background: var(--bg);
  }
  .ad-canvas {
    position: relative;
    width: 1200px;
    height: 628px;
    background: var(--bg);
    overflow: hidden;
    font-family: "Source Sans 3", sans-serif;
  }
  .hero-photo {
    position: absolute;
    left: 480px;
    top: 0;
    width: 720px;
    height: 628px;
    background:
      radial-gradient(ellipse 38% 42% at 55% 48%, rgba(210,200,220,0.55) 0%, rgba(120,60,120,0.35) 45%, transparent 75%),
      radial-gradient(ellipse 55% 60% at 60% 50%, var(--glow-blue) 0%, transparent 70%),
      radial-gradient(ellipse 75% 80% at 58% 52%, var(--glow-red) 0%, var(--glow-violet) 35%, transparent 72%);
    opacity: 0.95;
  }
  .message {
    position: absolute;
    left: 64px;
    top: 228px;
  }
  .message__headline {
    color: var(--headline);
    font-weight: 700;
    font-size: 74px;
    line-height: 1;
    letter-spacing: 0.5px;
    white-space: nowrap;
  }
  .message__tagline {
    color: var(--tagline);
    font-weight: 400;
    font-size: 54px;
    line-height: 1;
    margin-top: 7px;
    white-space: nowrap;
  }
  .brand-plate {
    position: absolute;
    left: 798px;
    top: 478px;
    width: 402px;
    height: 98px;
  }
  .brand-plate svg { position: absolute; inset: 0; }
  .brand-plate__name {
    position: absolute;
    left: 70px;
    top: 0;
    height: 98px;
    display: flex;
    align-items: center;
    gap: 14px;
    color: var(--brand);
    font-weight: 700;
    font-size: 48px;
  }
  .brand-plate__dot {
    width: 22px;
    height: 22px;
    border-radius: 50%;
    background: var(--brand);
  }
</style>
</head>
<body>
  <main class="ad-canvas">
    <div class="hero-photo" role="img" aria-label="Motorcycle racer leaning into a corner on a race bike, wrapped in glowing red, violet and blue light trails against a dark starry background"></div>

    <section class="message">
      <h1 class="message__headline">NEED A BANNER</h1>
      <p class="message__tagline">We make it Swift and Easy</p>
    </section>

    <div class="brand-plate">
      <svg width="402" height="98" viewBox="0 0 402 98" aria-hidden="true">
        <polygon points="22,0 402,0 402,98 0,98" fill="var(--plate)"/>
      </svg>
      <div class="brand-plate__name">
        <span class="brand-plate__dot"></span>
        <span>SwiftPress</span>
      </div>
    </div>
  </main>
</body>
</html>
```